Flyer Design Project for our Parenting Psychologists at the Bright Harbour Wellbeing Clinic

At the Bright Harbour Wellbeing Clinic we have expert Parenting Psychologists.

Parenting Psychologists provide practical, step by step assistance to parents who are struggling with their children's behavioural and emotional problems.

We need a DL size brochure that will be appealing to parents. The brochure will be on show in schools, kindergartens and GP clinics.

In terms of style it will be in line with our website and stationery that I will attach.

www.brightharbourwellbeing.com.au
Updates

Hi Everyone,
Thanks for putting forward your proposals, there are a couple there that I am very interested in. I am looking to see if there is a way that I can change my brief to guaranteed as I am definitely going to be using one of the designs for sure.
I have emailed ArtFolkly and as soon as I get an answer I will change it if I can.
If anyone out there already knows the answer please let me know :-)
Thanks,
Marnie.

Hi Again,

I worked it out myself!!

I have now changed this to a committed project.

Kind regards,
Marnie.

Reason: I have 46 designs now and need more time to work out which is best!

Target Market(s)

The target will be educated professional parents motivated to get professional help. And doctors and teachers who will pass on the brochures 2 parents

Industry/Entity Type

Health

Requirements
Must have
• I want one DL size brochure. Back and front.

We need text (below) and our contact details. Our logo.

9362 4158
Suite 1, 2071 Pellbrook Rd, Ferndale Heights 3109

Text:
Parents want the best for their kids. They want kids that are happy, healthy and well behaved.

So why is it so hard? Parents of toddlers, primary schoolers and teenagers alike say that they are frustrated by constant nagging, bribing and yelling, they don't know what to try next. Some parents worry that their children are unhappy. Struggling at school, not making friends or coping with bigger problems.

The good news is that getting your children to behave more co-operatively doesn't need to be difficult or mysterious. We all know that kids don't come with manuals, but there are skills every parent can learn to make parenting easier. In a few sessions with a Parenting Psychologist, you will receive step by step guidance in how to talk to your children in a way that will be much more effective getting them to behave in a respectful and co-operative way around the home and in public. You will learn how to help your child cope with problems they are going through. They can help you reconnect with your kids so you can enjoy being a parent again.

Nice to have
• Themes consistent with our website
and letterhead, business cards. I will attach these.
Should not have
• I don't want it to look too cluttered so if the text I have provided up above looks too crowded then I will edit it.

```html
<!DOCTYPE html>
<html lang="en">
<head>
<meta charset="utf-8">
<title>Bright Harbour Wellbeing Clinic – Parenting DL Brochure</title>
<link rel="stylesheet" href="https://fonts.googleapis.com/css2?family=Arimo:ital,wght@0,400;0,700;1,700&family=Roboto+Condensed:wght@700&family=Crimson+Pro:wght@700&display=swap">
<style>
  :root {
    --stage: #000000;
    --green: #0f7460;
    --ink: #1f1f1f;
    --white: #ffffff;
    --slate: #474e57;
    --brand-text: #e6e9ef;
    --lilac-top: #d8dcea;
    --lilac-bottom: #b9c1dc;
    --band-1: #6f9fb0;
    --band-2: #80c5ca;
    --band-3: #73a8a8;
    --band-4: #7b8a91;
    --band-5: #80c5ca;
    --photo-top: #7fa35a;
    --photo-bottom: #b87a5a;
  }
  * { margin: 0; padding: 0; box-sizing: border-box; }
  html, body { width: 1200px; height: 1176px; overflow: hidden; background: var(--stage); }
  body { position: relative; font-family: "Arimo", Arial, sans-serif; }

  .panel { position: absolute; top: 81px; width: 467px; height: 987px; }
  .panel--back { left: 111px; background: var(--green); }
  .panel--front { left: 635px; background: var(--stage); }

  .band { position: absolute; left: 0; width: 100%; display: flex; }
  .band span { flex: 1; }
  .band span:nth-child(1) { background: var(--band-1); }
  .band span:nth-child(2) { background: var(--band-2); }
  .band span:nth-child(3) { background: var(--band-3); }
  .band span:nth-child(4) { background: var(--band-4); }
  .band span:nth-child(5) { background: var(--band-5); }

  /* Back */
  .intro {
    position: absolute; left: 33px; top: 66px; width: 406px;
    color: var(--white); font-size: 15.8px; line-height: 23.2px; text-align: justify;
  }
  .intro__lead { font-size: 29px; line-height: 30px; }
  .services {
    position: absolute; left: 28px; top: 431px; width: 413px; height: 200px;
    border-radius: 14px; padding: 14px 16px;
    background: linear-gradient(90deg, #a3abc6 0%, #dfe3ee 100%);
    color: var(--ink);
  }
  .services__intro { font-size: 19px; line-height: 24px; }
  .services__list { list-style: none; margin-top: 10px; }
  .services__list li {
    font-family: "Roboto Condensed", "Arial Narrow", sans-serif; font-weight: 700;
    font-size: 25px; line-height: 36px; display: flex; align-items: center; gap: 12px;
  }
  .services__list svg { width: 20px; height: 20px; flex: none; }
  .contact { position: absolute; left: 0; width: 100%; text-align: center; color: var(--white); }
  .contact__label { top: 669px; font-size: 19px; }
  .contact__phone {
    top: 696px; font-family: "Roboto Condensed", "Arial Narrow", sans-serif;
    font-weight: 700; font-size: 42px;
  }
  .contact__mark { top: 766px; display: flex; justify-content: center; }
  .contact__name { top: 838px; font-weight: 700; font-size: 22px; }
  .contact__address { top: 874px; font-size: 16.5px; line-height: 21px; letter-spacing: 0.3px; }
  .contact__email { top: 921px; font-size: 15.5px; }

  /* Front */
  .hero {
    position: absolute; left: 0; top: 0; width: 100%; height: 314px;
    background: linear-gradient(160deg, #a9c47a 0%, var(--photo-top) 45%, var(--photo-bottom) 100%);
  }
  .message {
    position: absolute; left: 0; top: 329px; width: 100%; height: 407px;
    background: linear-gradient(180deg, var(--lilac-top), var(--lilac-bottom));
    text-align: center; color: var(--ink);
  }
  .message__title {
    margin-top: 18px; font-family: "Roboto Condensed", "Arial Narrow", sans-serif;
    font-weight: 700; font-size: 38px; line-height: 47px; text-transform: uppercase;
  }
  .message__sub {
    margin-top: 4px; font-family: "Crimson Pro", Georgia, serif; font-weight: 700;
    font-size: 30px; line-height: 39px;
  }
  .message__body {
    margin: 42px 30px 0; font-size: 15.2px; line-height: 23.5px; text-align: justify;
  }
  .signoff {
    position: absolute; left: 0; top: 748px; width: 100%; height: 197px; background: var(--slate);
  }
  .signoff__brand {
    position: absolute; left: 62px; top: 26px; display: flex; align-items: center; gap: 22px;
    color: var(--brand-text); font-size: 23px; line-height: 28px; letter-spacing: 3px; text-transform: uppercase;
  }
  .signoff__web {
    position: absolute; left: 0; bottom: 16px; width: 100%; text-align: center;
    color: var(--white); font-family: "Roboto Condensed", "Arial Narrow", sans-serif;
    font-weight: 700; font-size: 23px; letter-spacing: 0.6px;
  }

  .side-label {
    position: absolute; top: 1085px; width: 467px; text-align: center;
    color: var(--white); font-weight: 700; font-style: italic; font-size: 43px;
  }
</style>
</head>
<body>

<section class="panel panel--back" aria-label="Brochure back">
  <div class="band" style="top:0;height:40px"><span></span><span></span><span></span><span></span><span></span></div>

  <p class="intro"><span class="intro__lead">The good news is that</span> getting your children to behave more co-operatively doesn't need to be difficult or mysterious. We all know that kids don't come with manuals, but there are skills every parent can learn to make parenting easier. In a few sessions with a Parenting Psychologist, you will receive step by step guidance in how to talk to your children in a way that will be much more effective getting them to behave in a respectful and co-operative way around the home and in public. You will learn how to help your child cope with problems they are going through. They can help you reconnect with your kids so you can enjoy being a parent again.</p>

  <div class="services">
    <p class="services__intro">Our expert psychology team has specific training and experience in three key areas:</p>
    <ul class="services__list">
      <li><svg viewBox="0 0 20 20"><circle cx="10" cy="10" r="7" fill="none" stroke="#0f7460" stroke-width="2.5"/></svg>Disordered Eating</li>
      <li><svg viewBox="0 0 20 20"><circle cx="10" cy="10" r="7" fill="none" stroke="#0f7460" stroke-width="2.5"/></svg>Chronic Pain &amp; Illness</li>
      <li><svg viewBox="0 0 20 20"><circle cx="10" cy="10" r="7" fill="none" stroke="#0f7460" stroke-width="2.5"/></svg>Pregnancy &amp; Parenting</li>
    </ul>
  </div>

  <p class="contact contact__label">Appointment &amp; Enquiries</p>
  <p class="contact contact__phone">(03) 9362 4158</p>
  <div class="contact contact__mark"><svg width="60" height="60" viewBox="0 0 60 60"><circle cx="30" cy="30" r="27" fill="#0b5e4e"/></svg></div>
  <p class="contact contact__name">Bright Harbour Wellbeing Clinic</p>
  <p class="contact contact__address">Level 2, 2071 Pellbrook Road,<br>Ferndale Heights&nbsp; Westmere&nbsp; 4826</p>
  <p class="contact contact__email">email: info@brightharbourwellbeing.com.au</p>

  <div class="band" style="top:948px;height:39px"><span></span><span></span><span></span><span></span><span></span></div>
</section>

<section class="panel panel--front" aria-label="Brochure front">
  <div class="hero" role="img" aria-label="Photo of a mother and toddler on a picnic blanket in a sunny park"></div>
  <div class="band" style="top:314px;height:15px"><span></span><span></span><span></span><span></span><span></span></div>

  <div class="message">
    <h1 class="message__title">Parents want the<br>best for their kids.</h1>
    <p class="message__sub">They want kids that are happy,<br>healthy and well behaved.</p>
    <p class="message__body">So why is it so hard? Parents of toddlers, primary schoolers and teenagers alike say that they are frustrated by constant nagging, bribing and yelling, they don't know what to try next. Some parents worry that their children are unhappy. Struggling at school, not making friends or coping with bigger problems.</p>
  </div>

  <div class="band" style="top:736px;height:12px"><span></span><span></span><span></span><span></span><span></span></div>

  <div class="signoff">
    <div class="signoff__brand">
      <svg width="80" height="80" viewBox="0 0 80 80"><circle cx="40" cy="40" r="36" fill="none" stroke="#e6e9ef" stroke-width="5"/></svg>
      <span>Bright Harbour<br>Wellbeing<br>Clinic</span>
    </div>
    <p class="signoff__web">www.brightharbourwellbeing.com.au</p>
  </div>

  <div class="band" style="top:948px;height:39px"><span></span><span></span><span></span><span></span><span></span></div>
</section>

<p class="side-label" style="left:111px">BACK</p>
<p class="side-label" style="left:635px">FRONT</p>

</body>
</html>
```